Creative flyer for small business IT services

We are an IT services company based in Western Australia. We're looking to expand our market share amongst small businesses and need a brochure/flyer designed to give them a good overview of why we can help them. The design and layout should be consistent with an existing company profile brochure (included) but please be creative. A comprehensive brief with copy and a rough layout is included.

Small Business

```html
<!DOCTYPE html>
<html lang="en">
<head>
<meta charset="utf-8">
<title>Small Business IT Solutions – TileBeta</title>
<link rel="stylesheet" href="https://fonts.googleapis.com/css2?family=Source+Sans+3:wght@300;400;600;700&display=swap">
<style>
:root{
  --red:#b0121b;
  --red-dark:#8c0c13;
  --ink:#222;
  --body:#555;
  --page:#ffffff;
  --stage:#e9e8e6;
  --box-grey:#d9d9d9;
  --lavender:#e4e1ee;
  --pink:#f4dde1;
  --grey-panel:#d6d6d8;
  --blue:#d9e8f4;
  --peach:#f6e2d2;
  --ring-pink:#ee9aa4;
  --ring-lav:#c8c2dc;
  --ring-grey:#a9a9ac;
  --ring-blue:#8fc3e8;
  --ring-peach:#f3c27f;
}
*{margin:0;padding:0;box-sizing:border-box}
html,body{width:1200px;height:1148px;overflow:hidden;background:var(--stage)}
body{font-family:"Source Sans 3",Arial,sans-serif;color:var(--ink)}
.flyer{position:absolute;left:199px;top:24px;width:802px;height:1100px;background:var(--page);overflow:hidden;box-shadow:0 2px 10px rgba(0,0,0,.12)}
.header{position:absolute;left:0;top:0;width:100%;height:175px;background:linear-gradient(100deg,var(--red) 0%,#c41a22 45%,var(--red-dark) 100%)}
.header-title{position:absolute;left:52px;top:112px;color:#fff;font-size:33px;font-weight:300;letter-spacing:-.3px}
.header-title b{font-weight:700}
.brand-mark{position:absolute;left:580px;top:31px;width:84px;height:84px;background:#fff}
.brand-name{position:absolute;left:556px;top:118px;width:132px;text-align:center;color:#fff;font-size:16px;font-weight:400}
.intro{position:absolute;left:0;top:175px;width:100%;height:210px;background:linear-gradient(#fff,#efefef)}
.intro h1{position:absolute;left:62px;top:36px;font-size:26px;font-weight:700;letter-spacing:-.3px}
.intro p{position:absolute;left:62px;top:66px;font-size:26px;font-weight:300;color:#333}
.seedlings{position:absolute;left:192px;top:108px;width:503px;height:90px;background:linear-gradient(180deg,#f3f5ef 0%,#cfe3a8 40%,#6a4a31 80%,#f2f2f2 100%)}
.rule{position:absolute;left:0;top:385px;width:100%;height:8px;background:var(--red)}
.why{position:absolute;left:76px;top:418px;width:370px}
.why h2{font-size:22px;font-weight:700}
.why h3{font-size:22px;font-weight:300;margin-top:-4px}
.why p{font-size:12.5px;line-height:1.55;color:var(--body);margin-top:12px}
.reasons{position:absolute;left:467px;top:402px;width:250px;height:144px;background:var(--box-grey);padding:12px 14px}
.reasons h4{font-size:13px;font-weight:700;line-height:1.2;margin:0 0 8px 22px}
.reasons li{list-style:none;font-size:9.5px;color:#444;display:flex;align-items:center;gap:8px;height:23px;white-space:nowrap}
.reasons svg{flex:none}
.wheel{position:absolute;left:0;top:0}
.panel{position:absolute;font-size:8.6px;line-height:1.35;color:#555}
.panel h5{color:var(--red);font-size:13px;font-weight:700;margin-bottom:4px}
.panel p+p{margin-top:6px}
.p-monitor{left:86px;top:588px;width:215px}
.p-hardware{left:292px;top:582px;width:226px;text-align:center}
.p-hardware p{padding:0 22px}
.p-hardware p.narrow{padding:0 46px}
.p-audit{left:495px;top:578px;width:222px;text-align:right}
.p-audit p{text-align:center}
.p-support{left:88px;top:760px;width:198px}
.p-testi{left:498px;top:734px;width:220px;text-align:right}
.p-testi p{text-align:center}
.footer-lead{position:absolute;left:62px;top:956px;font-size:13px;color:#444}
.footer-row{position:absolute;left:62px;top:986px;width:680px;height:50px;display:flex;align-items:center}
.footer-brand{display:flex;align-items:center;gap:8px;font-size:17px;color:#333;width:160px}
.footer-brand span.sq{width:24px;height:24px;background:var(--red)}
.footer-cell{border-left:2px solid var(--red);padding-left:22px;height:40px;display:flex;flex-direction:column;justify-content:center;font-size:10.5px;color:#444}
.footer-cell.addr{width:180px;align-items:center;text-align:center}
.footer-cell.web{width:170px}
.footer-cell.web b{font-weight:700}
.footer-cell.phone{font-size:19px;font-weight:700;color:#222}
.footer-band{position:absolute;left:0;top:1052px;width:100%;height:48px;background:var(--red)}
</style>
</head>
<body>
<main class="flyer">
  <header class="header">
    <div class="header-title"><b>Small Business</b> IT Solutions</div>
    <div class="brand-mark"></div>
    <div class="brand-name">tilebeta</div>
  </header>

  <section class="intro">
    <div class="seedlings" role="img" aria-label="Row of seedlings growing taller from small mounds of soil"></div>
    <h1>Small business. Big ideas.</h1>
    <p>We’ll help your business grow.</p>
  </section>
  <div class="rule"></div>

  <section class="why">
    <h2>We help small businesses</h2>
    <h3>get ahead of the pack.</h3>
    <p>You’ve always got more to do. In a small business, the last thing you need is another hat to wear. You shouldn’t need to become a computer engineer to keep your business running smoothly. Say goodbye to IT headaches – our mission is to make your life easier.</p>
  </section>

  <aside class="reasons">
    <h4>Here’s why small businesses<br>love TileBeta:</h4>
    <ul>
      <li><svg width="12" height="12" viewBox="0 0 12 12"><path d="M1 6.5 4.5 10 11 1.5" fill="none" stroke="#b0121b" stroke-width="2.2"/></svg>We’re small business IT experts</li>
      <li><svg width="12" height="12" viewBox="0 0 12 12"><path d="M1 6.5 4.5 10 11 1.5" fill="none" stroke="#b0121b" stroke-width="2.2"/></svg>We speak plain English and won’t waste your time</li>
      <li><svg width="12" height="12" viewBox="0 0 12 12"><path d="M1 6.5 4.5 10 11 1.5" fill="none" stroke="#b0121b" stroke-width="2.2"/></svg>We care about our relationships</li>
      <li><svg width="12" height="12" viewBox="0 0 12 12"><path d="M1 6.5 4.5 10 11 1.5" fill="none" stroke="#b0121b" stroke-width="2.2"/></svg>We worry about IT so you don’t have to</li>
    </ul>
  </aside>

  <svg class="wheel" width="802" height="940" viewBox="0 0 802 940" aria-hidden="true">
    <polygon points="78,598 268,572 352,790 300,815 78,720" fill="var(--lavender)"/>
    <polygon points="78,740 296,830 318,912 78,930" fill="var(--pink)"/>
    <polygon points="282,570 542,570 450,790 354,790" fill="var(--grey-panel)"/>
    <polygon points="548,572 724,560 724,700 500,800 458,790" fill="var(--blue)"/>
    <polygon points="508,815 724,715 724,890 520,912" fill="var(--peach)"/>
    <g stroke="#fff" stroke-width="3">
      <path d="M277,912 A125,125 0 0 1 293.7,849.5 L319.7,864.5 A95,95 0 0 0 307,912 Z" fill="var(--ring-pink)"/>
      <path d="M293.7,849.5 A125,125 0 0 1 349.1,798.7 L361.8,825.9 A95,95 0 0 0 319.7,864.5 Z" fill="var(--ring-lav)"/>
      <path d="M349.1,798.7 A125,125 0 0 1 454.9,798.7 L442.2,825.9 A95,95 0 0 0 361.8,825.9 Z" fill="var(--ring-grey)"/>
      <path d="M454.9,798.7 A125,125 0 0 1 510.3,849.5 L484.3,864.5 A95,95 0 0 0 442.2,825.9 Z" fill="var(--ring-blue)"/>
      <path d="M510.3,849.5 A125,125 0 0 1 527,912 L497,912 A95,95 0 0 0 484.3,864.5 Z" fill="var(--ring-peach)"/>
    </g>
    <path d="M307,912 A95,95 0 0 1 497,912 Z" fill="var(--red)"/>
    <g fill="#fff">
      <ellipse cx="358" cy="856" rx="11" ry="4"/>
      <rect x="347" y="856" width="22" height="16"/>
      <ellipse cx="358" cy="872" rx="11" ry="4"/>
      <circle cx="402" cy="842" r="11"/>
      <circle cx="402" cy="842" r="4.5" fill="var(--red)"/>
      <rect x="436" y="858" width="5" height="14"/>
      <rect x="444" y="850" width="5" height="22"/>
      <rect x="452" y="862" width="5" height="10"/>
      <path d="M430,888 h24 a4,4 0 0 1 4,4 v10 a4,4 0 0 1 -4,4 h-14 l-6,5 v-5 h-4 a4,4 0 0 1 -4,-4 v-10 a4,4 0 0 1 4,-4 z"/>
    </g>
  </svg>

  <div class="panel p-monitor">
    <h5>Monitoring &amp; Backup</h5>
    <p>Most of us insure our cars and homes, yet small businesses often don’t protect themselves from the kind of disaster that strikes every day. Could your business recover from the complete loss of every electronic file – financial records, legal documents, customer information, archives, emails and more?</p>
    <p style="padding-left:40px">Our Monitor &amp; Protect solutions keep you safe from physical threats like theft, fire and floods, but also from electronic threats like viruses and hackers. It all happens automatically, so you can relax.</p>
  </div>

  <div class="panel p-hardware">
    <h5>Hardware &amp; Software</h5>
    <p>Every business needs the right tools for the job. We supply world class hardware and software products from Northsoft, Helio, Ivra, Pomelo, Ciro, Adara, Voltcore and many more. Our strong partnerships and buying power mean we can save you money.</p>
    <p class="narrow">From a single keyboard to an entire infrastructure, we always take the time to help you select the right products.</p>
  </div>

  <div class="panel p-audit">
    <h5>Audit</h5>
    <p>It helps to know where you stand.</p>
    <p>Get a clearer picture of your IT systems with our obligation-free IT audit and consultation.</p>
    <p>Contact us today and we’ll provide you with expert insights into how your business can benefit from today’s amazing technology.</p>
  </div>

  <div class="panel p-support">
    <h5>Support Services</h5>
    <p>Say goodbye to IT interruptions, slow services, confusing jargon and inexplicable errors. We have solutions to your IT problems, and packages to suit every budget. We can even come to your workplace. If you run into a problem or need something done, just contact our Service Desk.</p>
    <p>Whether you have a single computer or a big team with complex requirements, our expert team can assist. We’ll give you an entire IT department for a fraction of the cost.</p>
  </div>

  <div class="panel p-testi">
    <h5>Testimonials</h5>
    <p>Don’t just take our word for it! Here’s what some satisfied customers have to say about TileBeta:</p>
    <p>“We are pleased to have TileBeta as part of our team. I recommend them for any business seeking a trustworthy, reliable and effective IT service provider.” <b>– Lena Marsh, Coastline Imaging</b></p>
    <p>“TileBeta’s expertise has allowed us to test, analyse and improve the reliability and performance of our application.” <b>– Tom Reyes, Gradebook Pty Ltd</b></p>
  </div>

  <p class="footer-lead">Our valued customers are already enjoying the benefits of partnering with TileBeta. Join them by contacting us today:</p>
  <footer class="footer-row">
    <div class="footer-brand"><span class="sq"></span>tilebeta</div>
    <div class="footer-cell addr"><span>Level 12, 88 Harbour Row</span><span>Westport WA 6100</span></div>
    <div class="footer-cell web"><span>sales@tilebeta.com.au</span><b>www.tilebeta.com.au</b></div>
    <div class="footer-cell phone">1300 555 018</div>
  </footer>
  <div class="footer-band"></div>
</main>
</body>
</html>
```